The Cactus Lantern Food Truck, Specializes in Tacos, Quesadillas, Burritos The Cactus Lantern Dog and The Cactus Lantern Bowl, which is all the ingredients of a burrito mixed in a bowl. Meat options include Steak, Chicken, Shrimp and Pork. Attached fins a Picture of our food truck. we want to keep that color scheme

Colors
9bcb3c
ec1f27

Requirements
Must have
• Pictures of all the items we offer, main colors for the design should be lime bright green and red. font should be easily readable.
Nice to have
• picture of a lime green food truck

```html
<!DOCTYPE html>
<html lang="en">
<head>
<meta charset="utf-8">
<title>The Cactus Lantern Food Truck</title>
<link rel="stylesheet" href="https://fonts.googleapis.com/css2?family=Bebas+Neue&family=Montserrat:wght@700&family=Roboto+Condensed:wght@800&display=swap">
<style>
  :root {
    --lime: #9bcb3c;
    --red: #ec1f27;
    --panel-red: #e1352a;
    --ink: #2b2624;
    --white: #ffffff;
    --taco-light: #e8c98a;
    --taco-dark: #8a5a34;
  }
  html, body {
    margin: 0;
    padding: 0;
    width: 848px;
    height: 1200px;
    overflow: hidden;
    background: var(--lime);
  }
  .canvas {
    position: relative;
    width: 848px;
    height: 1200px;
    overflow: hidden;
    background: var(--lime);
  }
  /* the flyer is laid out landscape, then turned a quarter clockwise */
  .sheet {
    position: absolute;
    left: 0;
    top: 0;
    width: 1200px;
    height: 848px;
    transform-origin: 0 0;
    transform: translate(848px, 0) rotate(90deg);
  }
  .hat-mark {
    position: absolute;
    left: 208px;
    top: 71px;
    width: 192px;
    height: 123px;
    border-radius: 96px 96px 12px 12px;
    background: var(--red);
  }
  .title {
    position: absolute;
    left: 10px;
    top: 214px;
    width: 600px;
    margin: 0;
    text-align: center;
    font-family: "Roboto Condensed", "Arial Narrow", sans-serif;
    font-weight: 800;
    font-size: 90px;
    line-height: 80px;
    color: var(--red);
    text-transform: uppercase;
    white-space: nowrap;
  }
  .title span { display: block; height: 80px; }
  .title .title-name { font-size: 66px; letter-spacing: -1px; }
  .flourish {
    position: absolute;
    left: 101px;
    top: 496px;
    width: 401px;
    height: 88px;
    border-radius: 44px;
    background: linear-gradient(90deg, rgba(236,31,39,0.35), rgba(236,31,39,0.6), rgba(236,31,39,0.35));
  }
  .taco-photo {
    position: absolute;
    left: 48px;
    top: 590px;
    width: 513px;
    height: 221px;
    border-radius: 60px;
    background: linear-gradient(90deg, var(--taco-light), var(--taco-dark) 35%, #c9743f 55%, var(--taco-light) 80%, #d9a85a);
  }
  .events-panel {
    position: absolute;
    left: 673px;
    top: 95px;
    width: 438px;
    height: 657px;
  }
  .events-panel svg {
    position: absolute;
    inset: 0;
  }
  .truck-name {
    position: absolute;
    left: 100px;
    top: 52px;
    width: 160px;
    margin: 0;
    text-align: center;
    font-family: "Bebas Neue", "Arial Narrow", sans-serif;
    font-size: 18px;
    line-height: 18px;
    color: var(--lime);
  }
  .events-list {
    position: absolute;
    left: 0;
    top: 132px;
    width: 438px;
    margin: 0;
    text-align: center;
    font-family: "Bebas Neue", "Arial Narrow", sans-serif;
    font-size: 62px;
    line-height: 69px;
    color: var(--ink);
  }
  .events-list span { display: block; }
  .contact {
    position: absolute;
    left: 85px;
    top: 570px;
    margin: 0;
    font-family: "Montserrat", Arial, sans-serif;
    font-weight: 700;
    font-size: 14px;
    line-height: 21.5px;
    letter-spacing: 3px;
    color: var(--white);
    text-transform: uppercase;
    white-space: nowrap;
  }
  .contact span { display: block; }
</style>
</head>
<body>
<div class="canvas">
  <div class="sheet">
    <div class="hat-mark" role="img" aria-label="Red sombrero ornament"></div>
    <h1 class="title">
      <span>The</span>
      <span class="title-name">Cactus Lantern</span>
      <span>Food Truck</span>
    </h1>
    <div class="flourish" role="img" aria-label="Red curling swirl ornament"></div>
    <div class="taco-photo" role="img" aria-label="Photo of five tacos in a row with steak, chicken, shrimp and pork fillings"></div>

    <section class="events-panel">
      <svg width="438" height="657" viewBox="0 0 438 657" aria-hidden="true">
        <path d="M32 0 H406 A32 32 0 0 0 438 32 V625 A32 32 0 0 0 406 657 H32 A32 32 0 0 0 0 625 V32 A32 32 0 0 0 32 0 Z" fill="var(--panel-red)"/>
      </svg>
      <p class="truck-name">Cactus Lantern<br>Food Truck</p>
      <h2 class="events-list">
        <span>We Do</span>
        <span>Private</span>
        <span>Parties</span>
        <span>And</span>
        <span>Corporate</span>
        <span>Events</span>
      </h2>
      <p class="contact">
        <span>Tel. 973-555-0148</span>
        <span>Picstream and Friendpage</span>
        <span>@thecactuslanterntruck</span>
      </p>
    </section>
  </div>
</div>
</body>
</html>
```